Pell Nutrition Therapy needs a business card design

I need a business card design for my private practice. Green is my favorite color. I would like the back of the card to include an area for future appointment dates and time. I provide nutrition therapy to individuals, groups and families. I work a lot with adolescents and women who have eating disorders, but also work with athletes.

Reason: I received several new designs and would like to take some time reviewing them.

Target Market(s)

I am working primarily with women, but also men (mostly athletes). I work with a lot of runners. I work with people who are 14-60's.

Industry/Entity Type

Nutrition

Font styles to use
Serif
Sans Serif

Colors
9bcb3c
acd037

Requirements
Nice to have
• I would love to have 'Pell' incorporated into the design since it is my last name. If possible, I'd love to have an actual moon if it looks professional.

A picture of food could also be on the card if it is simple, but not sure how it would look with Pell. I am open to ideas for both Pell and a picture of a food item.

Other font style are fine as long as they are easy to read.

```html
<!DOCTYPE html>
<html lang="en">
<head>
<meta charset="utf-8">
<title>Pell Nutrition Therapy – Business Card</title>
<link href="https://fonts.googleapis.com/css2?family=Oswald:wght@500;600&family=Arimo:wght@700&display=swap" rel="stylesheet">
<style>
  :root {
    --canvas-bg: #ece9e4;
    --night-deep: #0d1f1a;
    --night-teal: #2f7a66;
    --night-glow: #8fd8c0;
    --title-dark: #14261d;
    --lime-light: #b6dc4a;
    --lime: #9bcb3c;
    --lime-deep: #7fb12c;
    --text-dark: #10240f;
    --badge: #f4f8e6;
    --food-warm: #d98a3c;
    --food-red: #b8452c;
    --food-light: #e9d5a8;
  }
  * { margin: 0; padding: 0; box-sizing: border-box; }
  html, body { width: 1200px; height: 900px; overflow: hidden; }
  body { background: var(--canvas-bg); position: relative; font-family: "Arimo", Arial, sans-serif; }

  .card {
    position: absolute;
    width: 540px;
    height: 309px;
    border-radius: 4px;
    overflow: hidden;
    box-shadow: 0 10px 28px rgba(0,0,0,.18);
  }

  /* Front */
  .card--front { left: 70px; top: 110px; }
  .front-scene {
    position: absolute; inset: 0;
    background:
      radial-gradient(circle at 34% 58%, rgba(190,235,215,.55) 0 70px, transparent 130px),
      radial-gradient(ellipse at 75% 60%, rgba(230,250,240,.8) 0, transparent 45%),
      linear-gradient(165deg, var(--night-teal) 0%, #1d4c40 45%, var(--night-deep) 100%);
  }
  .front-title {
    position: absolute;
    right: 28px; top: 128px;
    font-family: "Oswald", "Arial Narrow", sans-serif;
    font-weight: 600;
    font-size: 36px;
    letter-spacing: .5px;
    color: var(--title-dark);
    text-transform: uppercase;
  }

  /* Back */
  .card--back { left: 590px; top: 470px; background: linear-gradient(160deg, var(--lime-light) 0%, var(--lime) 55%, var(--lime-deep) 100%); }
  .back-food {
    position: absolute; top: 0; right: 0; bottom: 0; width: 150px;
    border-left: 3px solid #3f6b1e;
    background:
      radial-gradient(circle at 65% 28%, var(--food-light) 0 26px, transparent 40px),
      radial-gradient(circle at 40% 70%, var(--food-red) 0 30px, transparent 60px),
      linear-gradient(180deg, var(--food-light) 0%, var(--food-warm) 45%, var(--food-red) 100%);
  }
  .brand {
    position: absolute; left: 26px; top: 44px;
    display: flex; align-items: center; gap: 10px;
  }
  .brand-mark { width: 42px; height: 42px; border-radius: 50%; background: var(--badge); }
  .brand-name {
    font-family: "Oswald", "Arial Narrow", sans-serif;
    font-weight: 500; font-size: 27px;
    color: var(--text-dark); text-transform: uppercase;
  }
  .practitioner {
    position: absolute; left: 26px; top: 140px;
    font-size: 20px; color: var(--text-dark);
  }
  .practitioner .credentials { font-size: 14px; }
  .contact-list { position: absolute; left: 26px; top: 182px; list-style: none; }
  .contact-list li {
    display: flex; align-items: center; gap: 10px;
    font-size: 13px; color: var(--text-dark); line-height: 21px;
  }
  .contact-list svg { width: 14px; height: 14px; fill: var(--text-dark); flex: none; }
</style>
</head>
<body>

<section class="card card--front">
  <div class="front-scene" role="img" aria-label="Night landscape with a large pale full moon rising over dark forested hills under green light rays"></div>
  <h1 class="front-title">Pell Nutrition Therapy</h1>
</section>

<section class="card card--back">
  <div class="back-food" role="img" aria-label="Photo of assorted snack foods: chips, crackers, a burger and pasta"></div>
  <div class="brand">
    <span class="brand-mark"></span>
    <span class="brand-name">Pell Nutrition Therapy</span>
  </div>
  <p class="practitioner">Dara Whitfield Pell, <span class="credentials">MS, RD, LDN</span></p>
  <ul class="contact-list">
    <li><svg viewBox="0 0 24 24"><path d="M6.6 10.8a15 15 0 0 0 6.6 6.6l2.2-2.2a1 1 0 0 1 1-.25 11.4 11.4 0 0 0 3.6.57 1 1 0 0 1 1 1V20a1 1 0 0 1-1 1A17 17 0 0 1 3 4a1 1 0 0 1 1-1h3.5a1 1 0 0 1 1 1c0 1.25.2 2.45.57 3.57a1 1 0 0 1-.25 1z"/></svg>555.014.2290</li>
    <li><svg viewBox="0 0 24 24"><path d="M6 3h12v5H6zM3 9h18v9h-3v3H6v-3H3zm5 6v4h8v-4z"/></svg>555.014.7731</li>
    <li><svg viewBox="0 0 24 24"><path d="M2 5h20v14H2zm2 2v.5l8 5 8-5V7z"/></svg>dpell@mailbox.example</li>
    <li><svg viewBox="0 0 24 24"><path d="M12 3l10 9h-3v9h-5v-6h-4v6H5v-9H2z"/></svg>4410 Alder Bend Road, Fairview, TN 37000</li>
  </ul>
</section>

</body>
</html>
```